QM Studios needs and Interior Design Business card

I can do anything from Commercial to Residential and Free lance. Beginning to end in design selection process.
Need something to catch the eye of potential customers and vendors. From furniture to Tile and Cabinet selections. I can do it all.

Industry/Entity Type

Design Agency

Contact Information for Business Card

QM Studios- Design Consultanting Residential, Commerical
Maybe a cool detail background. Wall paper print that can have some texture

Font styles to use
Serif

Colors
709dcb
34a6d7
b868aa
e667a6
f59296
85acd3
ffffff
000000
5c5c5c

Requirements
Must have
• Square or Rectangular with Rounded edges
• Name
• Address
• Phone
• Email
Nice to have
• Some colored edges More simples not too busy
• Pattern detail in background.
Should not have
• Not too much color

```html
<!DOCTYPE html>
<html lang="en">
<head>
<meta charset="utf-8">
<title>QM Studios – Business Card</title>
<link href="https://fonts.googleapis.com/css2?family=Lato:wght@400;700&display=swap" rel="stylesheet">
<style>
  :root {
    --stage: #2a2a2a;
    --ink: #0b0a0b;
    --ink-soft: #1a181a;
    --paper: #ffffff;
    --paper-soft: #f3f2f3;
    --accent: #e23f9c;
    --text-light: #ffffff;
    --text-dark: #111111;
  }
  * { box-sizing: border-box; margin: 0; padding: 0; }
  html, body { width: 1200px; height: 1166px; overflow: hidden; }
  body {
    background: var(--stage);
    font-family: "Lato", sans-serif;
    position: relative;
  }
  .card {
    position: absolute;
    left: 320px;
    width: 560px;
    height: 320px;
    border-radius: 14px;
    overflow: hidden;
    box-shadow: 0 18px 40px rgba(0,0,0,.45);
  }
  .card--front { top: 213px; }
  .card--back { top: 633px; display: flex; }

  .texture {
    position: absolute; inset: 0;
  }
  .texture--dark { background: radial-gradient(circle at 50% 40%, var(--ink-soft), var(--ink)); }
  .texture--light { background: radial-gradient(circle at 50% 50%, var(--paper), var(--paper-soft)); }

  .brand {
    position: absolute;
    display: flex; flex-direction: column; align-items: center;
  }
  .brand__ring {
    width: 108px; height: 108px; border-radius: 50%;
    border: 4px solid currentColor;
  }
  .brand__name {
    margin-top: 20px;
    font-size: 40px;
    font-weight: 400;
    letter-spacing: 8px;
    white-space: nowrap;
  }
  .card--front .brand { left: 0; right: 0; top: 62px; color: var(--text-light); }

  .back__logo-side {
    position: relative; width: 42%; height: 100%;
    border-right: 3px solid var(--accent);
  }
  .back__logo-side .brand { left: 0; right: 0; top: 84px; color: var(--text-dark); }
  .back__logo-side .brand__ring { width: 86px; height: 86px; }
  .back__logo-side .brand__name { font-size: 26px; letter-spacing: 5px; margin-top: 16px; }

  .back__info-side {
    position: relative; flex: 1; height: 100%;
    color: var(--text-light);
  }
  .contact {
    position: absolute; left: 58px; top: 60px;
    font-size: 17px; line-height: 1.35;
  }
  .contact__name { font-size: 24px; font-weight: 400; }
  .contact__role { color: var(--accent); font-size: 18px; margin-bottom: 14px; }
  .contact__address { margin-bottom: 14px; }
  .contact__line { display: flex; align-items: center; gap: 10px; }
  .contact__line svg { width: 14px; height: 14px; fill: var(--accent); flex: none; }
</style>
</head>
<body>

<section class="card card--front" aria-label="Card front">
  <div class="texture texture--dark" role="img" aria-label="Black wallpaper-style overlapping circle pattern"></div>
  <div class="brand">
    <div class="brand__ring"></div>
    <div class="brand__name">QM Studios</div>
  </div>
</section>

<section class="card card--back" aria-label="Card back">
  <div class="back__logo-side">
    <div class="texture texture--light" role="img" aria-label="Faint light grey overlapping circle pattern"></div>
    <div class="brand">
      <div class="brand__ring"></div>
      <div class="brand__name">QM Studios</div>
    </div>
  </div>
  <div class="back__info-side">
    <div class="texture texture--dark" role="img" aria-label="Black wallpaper-style overlapping circle pattern"></div>
    <div class="contact">
      <p class="contact__name">Nora Vellamy</p>
      <p class="contact__role">Design Consultant</p>
      <p class="contact__address">4100 Elm Crest<br>Marlow TX 78000</p>
      <p class="contact__line">
        <svg viewBox="0 0 16 16" aria-hidden="true"><path d="M3 1l3 3-1.5 2a9 9 0 0 0 5.5 5.5L12 10l3 3-2 2C7 15 1 9 1 3z"/></svg>
        555 014 2290</p>
      <p class="contact__line">
        <svg viewBox="0 0 16 16" aria-hidden="true"><path d="M4 1h8v14H4zM5.5 3v8h5V3zM7 12.5h2v1H7z" fill-rule="evenodd"/></svg>
        555 014 2291</p>
      <p class="contact__line">
        <svg viewBox="0 0 16 16" aria-hidden="true"><path d="M1 3h14v10H1zM2 4l6 5 6-5" /></svg>
        nora@vellamy.com</p>
    </div>
  </div>
</section>

</body>
</html>
```